Road Construction Company needs business cards

We would like a new business card designed for our business.

We're a road construction company based in Qld, Australia.

Can the business card please have the following information on it.

Name: Brent Malvoy
Position: General Manager
Phone: 0471 592 304
Email: Brent.malvoy@quendix.com.au
Address: 87 Harrowgate Ave, Pindarra, QLD, 4000
Website: www.quendix.com.au

Visually we'd like the card to be professional and simple.

Attached is our logo.

Our website is www.quendix.com.au

Target Market(s)

Men aged 25-60

Contact Information for Business Card

As listed in project description

Font styles to use
Serif

Requirements
Must have
• Large logo on back of card

```html
<!DOCTYPE html>
<html lang="en">
<head>
<meta charset="utf-8">
<title>Quendix Business Card</title>
<link rel="stylesheet" href="https://fonts.googleapis.com/css2?family=Open+Sans:wght@600;700;800&display=swap">
<style>
  :root {
    --backdrop: #5f5f5f;
    --brand-blue: #0b55a3;
    --ink-blue: #0d4a8f;
    --card-white: #ffffff;
    --logo-white: #ffffff;
  }
  * { box-sizing: border-box; margin: 0; padding: 0; }
  html, body {
    width: 1072px;
    height: 1200px;
    overflow: hidden;
    background: var(--backdrop);
    font-family: "Open Sans", Arial, sans-serif;
  }
  .card {
    position: absolute;
    top: 63px;
    width: 515px;
    height: 293px;
  }
  .card-back {
    left: 16px;
    background: var(--brand-blue);
    display: flex;
    align-items: center;
    justify-content: center;
  }
  .brand-name {
    color: var(--logo-white);
    font-weight: 800;
    font-size: 50px;
    letter-spacing: 2px;
    margin-top: -10px;
  }
  .card-front {
    left: 541px;
    background: var(--card-white);
    color: var(--ink-blue);
  }
  .identity {
    position: absolute;
    left: 20px;
    width: 155px;
    top: 133px;
    text-align: center;
  }
  .identity .person-name {
    font-size: 11px;
    font-weight: 700;
    letter-spacing: 0.3px;
  }
  .identity .person-role {
    font-size: 7px;
    font-weight: 600;
    margin-top: 3px;
  }
  .divider {
    position: absolute;
    left: 174px;
    top: 48px;
    width: 12px;
    height: 200px;
    background: linear-gradient(to right, rgba(0,0,0,0.10), rgba(0,0,0,0));
    -webkit-mask-image: linear-gradient(to bottom, transparent, #000 30%, #000 70%, transparent);
            mask-image: linear-gradient(to bottom, transparent, #000 30%, #000 70%, transparent);
  }
  .contact-list {
    position: absolute;
    left: 193px;
    top: 96px;
    list-style: none;
  }
  .contact-list li {
    display: flex;
    align-items: center;
    height: 26.5px;
    font-size: 10px;
    font-weight: 700;
    letter-spacing: 0.3px;
  }
  .contact-list svg {
    width: 10px;
    height: 10px;
    margin-right: 6px;
    flex: none;
  }
</style>
</head>
<body>
  <section class="card card-back" aria-label="Card back">
    <div class="brand-name">QUENDIX</div>
  </section>

  <section class="card card-front" aria-label="Card front">
    <div class="identity">
      <p class="person-name">Name: Brent Malvoy</p>
      <p class="person-role">Position: General Manager</p>
    </div>
    <div class="divider"></div>
    <ul class="contact-list">
      <li>
        <svg viewBox="0 0 10 10"><circle cx="5" cy="5" r="5" fill="#0d4a8f"/><path d="M3.3 2.6l1 1-.5.6c.4.8.9 1.3 1.7 1.7l.6-.5 1 1-.6.9c-1.9-.3-3.7-2.1-4-4z" fill="#fff"/></svg>
        Phone: 0471 592 304
      </li>
      <li>
        <svg viewBox="0 0 10 10"><circle cx="5" cy="5" r="5" fill="#0d4a8f"/><rect x="2.5" y="3.3" width="5" height="3.4" fill="#fff"/><path d="M2.5 3.3L5 5.2 7.5 3.3" stroke="#0d4a8f" stroke-width="0.6" fill="none"/></svg>
        Email: Brent.malvoy@quendix.com.au
      </li>
      <li>
        <svg viewBox="0 0 10 10"><circle cx="5" cy="5" r="5" fill="#0d4a8f"/><path d="M5 2.3L2.4 4.8h.8v2.8h1.3V5.8h1v1.8h1.3V4.8h.8z" fill="#fff"/></svg>
        Address: 87 Harrowgate Ave, Pindarra, QLD, 4000
      </li>
      <li>
        <svg viewBox="0 0 10 10"><circle cx="5" cy="5" r="5" fill="#0d4a8f"/><circle cx="5" cy="5" r="2.6" fill="none" stroke="#fff" stroke-width="0.7"/><path d="M2.4 5h5.2M5 2.4c-1.2 1.4-1.2 3.8 0 5.2M5 2.4c1.2 1.4 1.2 3.8 0 5.2" stroke="#fff" stroke-width="0.5" fill="none"/></svg>
        Website: www.quendix.com.au
      </li>
    </ul>
  </section>
</body>
</html>
```